Design new Brackwater Asset business card 2016

We need a new business card for our company Brackwater Asset Partners. We are a niche Alternative Investment Fund Manager based in Chester, in the North West of the UK.We market our services to global institutions such as banks, insurance companies, pension funds, etc. as well as wealthy individuals. Our main markets are Europe (Germany\France\Switzerland), the US and parts of Asia.
The design needs to be in line with existing company branding. Life the assets we deal with, the business card might suggest, "niche\alternative" type of attributes - however, it needs to remain professional, clean and appropriate for our client base.
Our existing business card format with relevant factual information is included, along with logo and branding details.

Target Market(s)

We market our services to global institutions such as banks, insurance companies, pension funds, etc. as well as wealthy individuals.

Industry/Entity Type

Financial Service

Contact Information for Business Card

please see attached pdf for information on existing business card which we should aim to convey on your new design. However:
- the wording "Brackwater Asset Partners Ltd is Authorised and Regulated
by the Monetary Oversight Bureau. Registered No. 7139046" should be replaced with , "Brackwater Asset Partners Ltd is an Alternative Investment Fund Manager Authorised and Regulated by the Monetary Oversight Bureau. Registered No. 7139046"
- the "reception" word on reverse can be omitted.
- the "retail: www.toplivanex.co.uk" wording can be omitted.
- the QR code is not required in the new version.

Font styles to use
Serif
Sans Serif

Requirements
Must have
• information on current business card, subject to comments provided above.
Nice to have
• Use of areas of solid colour instead of large areas of white space might be nice to experiment with. However, still need to have the general look and feel of the brand as presented on our website www.bwfundco.co.uk
• If we had space for 3 bullet points describing what we do\who we are, this might be good to try out. e.g. alternative investment fund manager, longevity specialist, founded 1990.
• Also, we have a new tag line, "Patience in every season" which might fit nicely somewhere on the business card.
Should not have
• - no QR code
• - should not use all the colours in our logo as it looks very garish! Using one or two colours with black\white etc, seems to work better.

```html
<!DOCTYPE html>
<html lang="en">
<head>
<meta charset="utf-8">
<title>Brackwater Asset Partners – Business Card</title>
<link rel="stylesheet" href="https://fonts.googleapis.com/css2?family=Lora:ital,wght@0,400;0,700;1,400&display=swap">
<style>
  :root {
    --page: #ece8e1;
    --brown: #5b3300;
    --olive: #9c9212;
    --olive-light: #c2b72a;
    --paper: #ffffff;
    --cream: #f6eedf;
    --ink: #5b3300;
  }
  * { box-sizing: border-box; margin: 0; padding: 0; }
  html, body {
    width: 1200px; height: 950px; overflow: hidden;
    background: var(--page);
    font-family: "Lora", Georgia, serif;
  }
  .canvas {
    width: 1200px; height: 950px;
    display: flex; flex-direction: column; align-items: center; justify-content: center;
    gap: 50px;
  }
  .card {
    position: relative;
    width: 700px; height: 400px;
    border-radius: 4px;
    overflow: hidden;
    box-shadow: 0 6px 18px rgba(60, 40, 10, 0.18);
  }

  /* Front */
  .card-front { background: var(--brown); }
  .front-top {
    position: absolute; inset: 0 0 auto 0; height: 170px;
    background: var(--paper);
    display: flex; align-items: center; justify-content: center; gap: 18px;
    padding-bottom: 20px;
  }
  .swoosh { position: absolute; left: 0; top: 120px; width: 700px; height: 80px; }
  .brand-mark {
    width: 56px; height: 56px; border-radius: 50%;
    background: var(--olive);
    flex: none;
  }
  .brand-name {
    font-size: 30px; font-weight: 400; color: var(--ink);
    letter-spacing: 0.5px;
  }
  .front-details {
    position: absolute; left: 70px; top: 206px;
    color: var(--cream);
  }
  .person-name { font-size: 22px; font-weight: 700; line-height: 1.3; }
  .person-role { font-size: 15px; line-height: 1.4; margin-bottom: 8px; }
  .contact-list { list-style: none; font-size: 15px; line-height: 1.45; }
  .contact-list li { display: flex; align-items: center; gap: 10px; }
  .contact-icon { width: 14px; height: 14px; flex: none; }
  .tagline { font-size: 15px; line-height: 1.45; margin-top: 6px; }

  /* Back */
  .card-back { background: var(--brown); color: var(--cream); }
  .back-brand {
    position: absolute; left: 56px; top: 48px;
    display: flex; align-items: center; gap: 14px;
  }
  .back-brand .brand-name { color: var(--cream); font-size: 32px; }
  .back-brand .brand-mark { width: 40px; height: 40px; background: var(--olive-light); }
  .service-list {
    position: absolute; left: 56px; top: 130px;
    list-style: none; font-style: italic; font-size: 17px; line-height: 1.6;
  }
  .service-list li::before { content: "• "; color: var(--olive-light); }
  .regulatory {
    position: absolute; left: 56px; bottom: 46px; width: 380px;
    font-style: italic; font-size: 13px; line-height: 1.5;
  }
</style>
</head>
<body>
<main class="canvas">

  <section class="card card-front" aria-label="Business card front">
    <div class="front-top">
      <span class="brand-mark"></span>
      <span class="brand-name">Brackwater Asset Partners</span>
    </div>
    <svg class="swoosh" viewBox="0 0 700 80" preserveAspectRatio="none" aria-hidden="true">
      <path d="M0 44 C 220 0, 480 8, 700 52 L700 80 L0 80 Z" fill="var(--olive)"/>
      <path d="M0 56 C 220 16, 480 24, 700 68 L700 80 L0 80 Z" fill="var(--brown)"/>
    </svg>
    <div class="front-details">
      <h1 class="person-name">Martin Hale</h1>
      <p class="person-role">Non-Executive Chairman</p>
      <ul class="contact-list">
        <li><svg class="contact-icon" viewBox="0 0 14 14"><path d="M3 1l2 3-1.5 1.5a7 7 0 0 0 5 5L10 9l3 2-1.5 2.5C6 13 1 8 .5 2.5z" fill="var(--cream)"/></svg>+44 (0)1632 480215</li>
        <li><svg class="contact-icon" viewBox="0 0 14 14"><rect x="3" y="1" width="8" height="12" rx="1.5" fill="none" stroke="var(--cream)" stroke-width="1.4"/></svg>+44 (0)7700 900417</li>
        <li><svg class="contact-icon" viewBox="0 0 14 14"><rect x="1" y="3" width="12" height="8" fill="none" stroke="var(--cream)" stroke-width="1.4"/><path d="M1 3l6 5 6-5" fill="none" stroke="var(--cream)" stroke-width="1.4"/></svg>mhale@bwfundco.co.uk</li>
        <li><svg class="contact-icon" viewBox="0 0 14 14"><circle cx="7" cy="7" r="6" fill="none" stroke="var(--cream)" stroke-width="1.4"/><path d="M1 7h12M7 1c3 3 3 9 0 12M7 1c-3 3-3 9 0 12" fill="none" stroke="var(--cream)" stroke-width="1"/></svg>www.bwfundco.co.uk</li>
      </ul>
      <p class="tagline">Patience in every season</p>
    </div>
  </section>

  <section class="card card-back" aria-label="Business card back">
    <div class="back-brand">
      <span class="brand-mark"></span>
      <span class="brand-name">Brackwater Asset Partners</span>
    </div>
    <ul class="service-list">
      <li>Alternative Investment Fund Manager</li>
      <li>Longevity Specialist</li>
      <li>Founded 1990</li>
    </ul>
    <p class="regulatory">Brackwater Asset Partners Ltd is an Alternative Investment Fund Manager Authorised and Regulated by the Monetary Oversight Bureau. Registered No. 7139046</p>
  </section>

</main>
</body>
</html>
```